Vellum Systemics Buisness Cards

I need a technology focused clean business card for my employees. I have attached out logo to include in the mocks. We're a modern tech consulting firm that drives to interface humanity with technology in a truly cohesive fashion.

```html
<!DOCTYPE html>
<html lang="en">
<head>
<meta charset="utf-8">
<title>Vellum Systemics Business Cards</title>
<link href="https://fonts.googleapis.com/css2?family=Arimo:wght@400;700&display=swap" rel="stylesheet">
<style>
  :root {
    --stage: #2e2e30;
    --brand-blue: #1f78c4;
    --brand-blue-dark: #1766a8;
    --card-white: #f4f4f4;
    --card-grey: #8c8d90;
    --card-grey-dark: #6f7073;
    --ink-grey: #6b6c6f;
    --ink-dark: #2f3033;
    --ink-light: #f1f1f1;
  }
  * { box-sizing: border-box; margin: 0; padding: 0; }
  html, body { width: 1200px; height: 997px; overflow: hidden; }
  body {
    background: var(--stage);
    font-family: "Arimo", Arial, sans-serif;
    position: relative;
  }

  .card {
    position: absolute;
    border-radius: 22px;
    overflow: hidden;
    box-shadow: 0 18px 40px rgba(0,0,0,0.45);
  }

  /* Back side */
  .card-back {
    left: 90px; top: 110px;
    width: 560px; height: 320px;
    background: linear-gradient(160deg, var(--brand-blue) 0%, var(--brand-blue-dark) 100%);
    display: flex; align-items: center; justify-content: center; gap: 16px;
  }
  .card-back .brand-dot {
    width: 46px; height: 46px; border-radius: 50%;
    border: 4px solid var(--ink-light);
  }
  .card-back .brand-name {
    color: var(--ink-light);
    font-weight: 700; font-size: 38px; letter-spacing: 1px;
  }

  /* Front side */
  .card-front {
    left: 520px; top: 500px;
    width: 620px; height: 354px;
    background: var(--card-white);
  }
  .card-front .wave { position: absolute; inset: 0; width: 100%; height: 100%; }
  .card-front .brand {
    position: absolute; left: 64px; top: 46px;
    display: flex; align-items: center; gap: 14px;
  }
  .card-front .brand-dot {
    width: 40px; height: 40px; border-radius: 50%;
    background: var(--brand-blue);
  }
  .card-front .brand-name {
    color: var(--ink-grey);
    font-weight: 700; font-size: 36px; letter-spacing: 0.5px;
  }
  .holder {
    position: absolute; left: 64px; top: 268px;
    color: var(--ink-light);
  }
  .holder-name { font-weight: 700; font-size: 17px; letter-spacing: 0.6px; text-transform: uppercase; }
  .holder-role { font-size: 14px; color: var(--ink-dark); margin-top: 3px; padding-left: 30px; }
  .divider {
    position: absolute; left: 318px; top: 200px;
    width: 1px; height: 120px; background: rgba(255,255,255,0.55);
  }
  .contact {
    position: absolute; left: 340px; top: 178px;
    color: var(--ink-dark); font-size: 12.5px; line-height: 1.45;
    list-style: none;
  }
  .contact .address { margin-bottom: 4px; }
  .contact li { display: flex; align-items: center; gap: 8px; }
  .contact .icon {
    width: 14px; height: 14px; border-radius: 50%;
    background: var(--brand-blue);
    display: inline-flex; align-items: center; justify-content: center;
    flex-shrink: 0;
  }
  .contact .icon svg { width: 9px; height: 9px; fill: #fff; }
</style>
</head>
<body>

  <section class="card card-back" aria-label="Card back">
    <span class="brand-dot"></span>
    <span class="brand-name">Vellum Systemics</span>
  </section>

  <section class="card card-front" aria-label="Card front">
    <svg class="wave" viewBox="0 0 620 354" preserveAspectRatio="none" aria-hidden="true">
      <defs>
        <linearGradient id="greyFill" x1="0" y1="0" x2="0" y2="1">
          <stop offset="0" stop-color="#9a9b9e"/>
          <stop offset="1" stop-color="#76777a"/>
        </linearGradient>
      </defs>
      <path d="M0,208 C150,240 300,222 420,152 C500,106 570,92 620,90 L620,354 L0,354 Z" fill="#1f78c4"/>
      <path d="M0,218 C150,250 300,234 420,164 C500,118 570,104 620,102 L620,354 L0,354 Z" fill="url(#greyFill)"/>
    </svg>

    <div class="brand">
      <span class="brand-dot"></span>
      <span class="brand-name">Vellum Systemics</span>
    </div>

    <div class="holder">
      <p class="holder-name">Marco Delaney</p>
      <p class="holder-role">Director</p>
    </div>

    <span class="divider"></span>

    <ul class="contact">
      <li class="address">Level 2, 14 Harbour Lane,<br>Eastwood Qld 4051</li>
      <li>
        <span class="icon"><svg viewBox="0 0 10 10"><path d="M2 1 L4 1 L4.6 3 L3.5 3.8 C4 5 5 6 6.2 6.5 L7 5.4 L9 6 L9 8 C9 8.6 8.6 9 8 9 C4.5 9 1 5.5 1 2 C1 1.4 1.4 1 2 1 Z"/></svg></span>
        1300 555 019
      </li>
      <li>
        <span class="icon"><svg viewBox="0 0 10 10"><path d="M1 2.5 H9 V7.5 H1 Z M1.5 3 L5 5.6 L8.5 3" stroke="#1f78c4" stroke-width="0.6"/></svg></span>
        hello@vellumsystemics.com
      </li>
      <li>
        <span class="icon"><svg viewBox="0 0 10 10"><circle cx="5" cy="5" r="3.8" fill="none" stroke="#fff" stroke-width="0.9"/><path d="M1.2 5 H8.8 M5 1.2 C3.4 3 3.4 7 5 8.8 M5 1.2 C6.6 3 6.6 7 5 8.8" fill="none" stroke="#fff" stroke-width="0.7"/></svg></span>
        www.vellumsystemics.com
      </li>
    </ul>
  </section>

</body>
</html>
```